PELDRAX Business Cards

We require a business card for our company that provides IT consulting services. We already have a logo that needs to be used on the card. We want a clean professional looking design that incorporates our colours. Our main focus is providing managed services to business, which involves us looking after all of their IT requirements including managing servers/networks, projects, and procurement.

Industry/Entity Type

Information Technology

Requirements
Must have
• our logo, contact information, name, title, phone numbers

```html
<!DOCTYPE html>
<html lang="en">
<head>
<meta charset="utf-8">
<title>PELDRAX Business Cards</title>
<link href="https://fonts.googleapis.com/css2?family=Source+Sans+3:wght@400;600&display=swap" rel="stylesheet">
<style>
  :root {
    --brand-blue: #0493cc;
    --card-grey: #f0f0f2;
    --ink: #2b2b2b;
    --page: #ffffff;
    --white: #ffffff;
    --shadow: rgba(0,0,0,0.55);
  }
  html, body {
    margin: 0;
    padding: 0;
    width: 1200px;
    height: 900px;
    overflow: hidden;
    background: var(--page);
    font-family: "Source Sans 3", sans-serif;
  }
  .canvas { position: relative; width: 1200px; height: 900px; }
  .card { position: absolute; box-shadow: 8px 9px 8px var(--shadow); overflow: hidden; }

  /* Front */
  .card-front {
    left: 85px; top: 52px; width: 628px; height: 358px;
    background: var(--brand-blue);
  }
  .front-brand {
    position: absolute; left: 38px; top: 108px;
    display: flex; align-items: center; gap: 28px;
  }
  .brand-dot { width: 110px; height: 110px; border-radius: 50%; background: var(--white); }
  .front-brand .brand-name {
    color: var(--white); font-weight: 600; font-size: 98px; letter-spacing: 6px; line-height: 1;
  }

  /* Back */
  .card-back {
    left: 402px; top: 466px; width: 625px; height: 359px;
    background: var(--card-grey);
  }
  .back-wave { position: absolute; left: 0; top: 0; }
  .holder-name {
    position: absolute; left: 31px; top: 31px; margin: 0;
    color: var(--brand-blue); font-weight: 400; font-size: 31px; line-height: 1; letter-spacing: 0.3px;
  }
  .holder-title {
    position: absolute; left: 32px; top: 68px; margin: 0;
    color: var(--ink); font-size: 16px;
  }
  .contact-line {
    position: absolute; left: 34px; display: flex; align-items: center; gap: 9px;
    color: var(--ink); font-size: 20px;
  }
  .contact-phone { top: 118px; }
  .contact-email { top: 164px; }
  .contact-line svg { width: 27px; height: 22px; fill: var(--brand-blue); }
  .address {
    position: absolute; left: 69px; top: 213px; margin: 0;
    color: var(--ink); font-size: 20px; line-height: 27px; font-style: normal;
  }
  .back-brand {
    position: absolute; left: 308px; top: 102px;
    display: flex; align-items: center; gap: 14px;
  }
  .back-brand .brand-dot { width: 62px; height: 62px; background: var(--brand-blue); }
  .back-brand .brand-name {
    color: var(--brand-blue); font-weight: 600; font-size: 46px; letter-spacing: 3px; line-height: 1;
  }
  .website {
    position: absolute; left: 419px; top: 306px;
    color: var(--white); font-size: 20px;
  }
</style>
</head>
<body>
<div class="canvas">

  <section class="card card-front">
    <div class="front-brand">
      <span class="brand-dot"></span>
      <span class="brand-name">PELDRAX</span>
    </div>
  </section>

  <section class="card card-back">
    <svg class="back-wave" width="625" height="359" viewBox="0 0 625 359">
      <path d="M0 285 C20 320 70 335 150 335 C300 335 430 270 625 268 L625 359 L0 359 Z" fill="var(--brand-blue)"/>
    </svg>

    <h1 class="holder-name">DANIEL HARWOOD</h1>
    <p class="holder-title">President &amp; Technology Consultant</p>

    <div class="contact-line contact-phone">
      <svg viewBox="0 0 27 22" aria-hidden="true">
        <path d="M2 6 C2 2 25 2 25 6 L25 8 L19 8 L19 5 L8 5 L8 8 L2 8 Z"/>
        <path d="M7 9 L20 9 L24 19 C24 20 23 21 22 21 L5 21 C4 21 3 20 3 19 Z"/>
      </svg>
      <span>403-555-0182</span>
    </div>

    <div class="contact-line contact-email">
      <svg viewBox="0 0 27 22" aria-hidden="true">
        <path d="M1 3 L26 3 L13.5 12 Z"/>
        <path d="M1 5 L13.5 14 L26 5 L26 20 L1 20 Z"/>
      </svg>
      <span>info@peldrax.com</span>
    </div>

    <address class="address">
      48 Elm Avenue<br>
      PO Box 2640<br>
      Ridgeford, AB<br>
      T0R 4B1
    </address>

    <div class="back-brand">
      <span class="brand-dot"></span>
      <span class="brand-name">PELDRAX</span>
    </div>

    <span class="website">www.peldrax.com</span>
  </section>

</div>
</body>
</html>
```